Homepage, Product & Category pages for E-commerce website

This website https://www.velmorgoods.ie/ is being ported to an ecommerce platform ( Wordpress&wooCommerce) we need a template design for the product pages and category pages
Each product will need to display multiple images, the complexity is that each product has a lot of additional extra's, size, color, labeling options and also 5-10 standard features for each. It's vital that we find a way to represent this information without overwhelming the user.
The Category pages should incorporate text and imagery and then incorporate the products within that category
The current homepage needs a lot of improving, I'm not a huge fan of every homepage having a massive slider so happy to think outside of the box here.
Target Market(s)
Councils, Hospitals, Distributors to these industries
Industry/Entity Type
Manufacture
Number of Pages Required
3 page
Font styles to use
Colors
Designer to choose colors to be used in the design.
Look and feel
Each slider illustrates characteristics of the customer's brand and the style your logo design should communicate.

```html
<!DOCTYPE html>
<html lang="en">
<head>
<meta charset="utf-8">
<title>Velmor Goods — Homepage, Product and Article templates</title>
<link href="https://fonts.googleapis.com/css2?family=Roboto:wght@300;400;500;700&display=swap" rel="stylesheet">
<style>
:root{
  --purple:#8b1a9e;
  --purple-dark:#6e1380;
  --purple-soft:#a63bb8;
  --lime:#a9c520;
  --lime-dark:#94ad16;
  --lime-soft:#c3da4e;
  --ink:#444;
  --muted:#8a8a8a;
  --line:#e3e3e3;
  --panel:#f1f1f1;
  --band:#ececec;
  --canvas:#e9e9e9;
  --white:#fff;
}
*{box-sizing:border-box;margin:0;padding:0}
html,body{width:1200px;height:1200px;overflow:hidden;background:var(--canvas);font-family:'Roboto',Arial,sans-serif;color:var(--ink)}
.stage{position:relative;width:1500px;height:1500px;transform:scale(.8);transform-origin:0 0}
.page{position:absolute;top:0;width:474px;background:var(--white);overflow:hidden}
.home{left:0;height:1500px}
.product{left:513px;height:680px}
.article{left:1026px;height:862px}
.a{position:absolute}
.tiny{font-size:4.2px;line-height:1.55;color:var(--muted)}
.small{font-size:5px;line-height:1.6;color:#777}
.bold{font-weight:700}

/* header */
.topbar{position:absolute;left:0;top:0;width:474px;height:34px;background:var(--purple)}
.brand{position:absolute;display:flex;align-items:center;gap:3px;background:var(--purple-dark);border:1px solid rgba(255,255,255,.5);padding:3px 5px;height:24px}
.brand i{display:block;width:12px;height:12px;background:var(--white)}
.brand span{color:var(--white);font-size:6.5px;font-weight:500;letter-spacing:.4px;line-height:1.1}
.toplink{position:absolute;top:4px;color:var(--white);font-size:3.6px;font-weight:500}
.searchbox{position:absolute;top:17px;height:11px;background:var(--white);font-size:3.6px;color:#999;padding:3px 4px}
.hbtn{position:absolute;top:17px;height:11px;background:var(--white);color:var(--purple);font-size:3.8px;font-weight:700;display:flex;align-items:center;justify-content:center}
.hcircle{position:absolute;top:18px;width:9px;height:9px;border-radius:50%;border:1.5px solid var(--white)}

.nav{position:absolute;top:44px;height:16px;background:var(--purple);color:var(--white);font-size:3.8px;font-weight:700;display:flex;align-items:center;justify-content:center}
.nav.on{background:var(--lime)}

/* side menu */
.sidemenu{position:absolute;left:37px;top:70px;width:95px;height:128px;border:1px solid #d9b6df;background:var(--white)}
.sidemenu div{position:absolute;left:6px;width:82px;height:14px;border-bottom:1px solid #f0e2f2;font-size:4.6px;color:var(--purple);display:flex;align-items:center;gap:4px}
.sidemenu div i{width:4px;height:4px;border:1px solid var(--purple);border-radius:50%}
.sidemenu div b{margin-left:auto;font-weight:400;color:#aaa}

.slider{position:absolute;left:139px;top:70px;width:298px;height:128px;background:linear-gradient(135deg,var(--purple) 0%,#b13cc4 55%,var(--purple) 100%)}
.slide-card{position:absolute;top:22px;width:80px;height:80px;background:var(--white);text-align:center}
.slide-card .ph{margin:6px auto 0;width:66px;height:44px}
.slide-card p{font-size:3.8px;color:var(--purple);margin-top:4px;line-height:1.4}
.slide-card em{font-style:normal;font-size:3.4px;color:var(--lime-dark)}
.dot{position:absolute;top:186px;width:4px;height:4px;border-radius:50%;background:var(--white)}

h2.sect{position:absolute;font-size:10px;font-weight:700;color:var(--purple);letter-spacing:.2px}
h2.center{left:0;width:474px;text-align:center;font-size:9.5px}

.social{position:absolute;left:308px;top:246px;width:129px;height:112px;background:var(--purple)}
.social .tile{position:absolute;width:40px;height:26px;border:1px solid rgba(255,255,255,.45);display:flex;flex-direction:column;align-items:center;justify-content:center;gap:3px}
.social .tile i{width:9px;height:9px;border:1px solid rgba(255,255,255,.7);border-radius:50%}
.social .tile span{font-size:2.8px;color:rgba(255,255,255,.8)}
.social .tile.on{background:var(--lime);border-color:var(--lime)}

.btn{position:absolute;height:13px;font-size:3.8px;font-weight:700;display:flex;align-items:center;justify-content:center}
.btn.outline{border:1px solid var(--purple);color:var(--purple)}
.btn.fill{background:var(--purple);color:var(--white)}

.feature{position:absolute;top:413px;width:130px;height:152px;background:var(--lime);overflow:hidden;text-align:center;color:var(--white)}
.feature .corner{position:absolute;right:-16px;top:-16px;width:40px;height:40px;border-radius:50%;background:var(--lime-soft)}
.feature .icon{margin:10px auto 0;width:24px;height:24px;border:1.5px solid var(--white);border-radius:50%}
.feature h3{margin-top:13px;font-size:7.5px;font-weight:700}
.feature .ph{margin:5px auto 0;width:32px;height:36px}
.feature p{margin:7px 8px 0;font-size:4px;line-height:1.55;color:#f5f9e0}
.feature b{display:block;margin-top:5px;font-size:3.6px}

.companies{position:absolute;left:37px;top:573px;width:400px;height:97px;background:#f3f3f3;overflow:hidden}
.companies .tri{position:absolute;left:0;top:0;width:0;height:0;border-top:20px solid var(--lime);border-right:20px solid transparent}
.company{position:absolute;top:612px;height:22px;width:56px;display:flex;align-items:center;justify-content:center;font-size:8.5px;font-weight:700;color:#555}

.blogband{position:absolute;left:0;top:698px;width:474px;height:247px;background:var(--band)}
.blogcard{position:absolute;top:750px;width:129px;height:143px;background:var(--white)}
.blogcard .ph{position:absolute;left:10px;top:10px;width:109px;height:58px}
.blogcard h4{position:absolute;left:10px;top:78px;font-size:4.6px;font-weight:500;color:#333}
.blogcard p{position:absolute;left:10px;top:88px;width:110px}
.blogcard em{position:absolute;left:10px;top:129px;font-style:normal;font-size:3.8px;color:var(--purple);font-weight:500}

.pcard{position:absolute;width:96px;height:125px;background:var(--white);border:1px solid var(--line)}
.pcard .ph{position:absolute;left:0;top:0;width:94px;height:60px;background:#f6f6f6}
.pcard .strip{position:absolute;left:0;top:60px;width:94px;height:15px;background:var(--lime);display:flex;gap:2px;padding:2px 3px}
.pcard .strip i{flex:1;background:var(--white)}
.pcard .stars{position:absolute;left:6px;top:81px;font-size:4px;color:var(--lime-dark);letter-spacing:.6px}
.pcard .rev{position:absolute;right:6px;top:82px;font-size:3px;color:#aaa}
.pcard h5{position:absolute;left:6px;top:91px;font-size:4px;font-weight:500;color:#333}
.pcard p{position:absolute;left:6px;top:99px;width:84px;font-size:3.3px;line-height:1.5;color:#999}

.badge{position:absolute;top:1305px;height:40px;background:#d0d0d0}

.footer{position:absolute;left:0;width:474px;background:var(--lime)}
.footer .brand{left:37px}
.footer h6{position:absolute;font-size:4.6px;font-weight:700;color:var(--white)}
.footer .links{position:absolute;font-size:3.4px;line-height:2.85;color:var(--white)}
.footer .addr{position:absolute;left:37px;font-size:3.3px;line-height:1.55;color:var(--white)}
.footer .field{position:absolute;height:9px;background:var(--white);border:1px solid #dfe8b8;font-size:3px;color:#aaa;padding:2px 3px}
.footer .send{position:absolute;height:8px;width:32px;background:var(--lime-dark);color:var(--white);font-size:3px;font-weight:700;display:flex;align-items:center;justify-content:center}
.footer .copy{position:absolute;left:0;width:474px;height:8px;background:var(--lime-dark);font-size:3px;color:var(--white);display:flex;align-items:center;justify-content:center}

/* product page */
.ptitle{position:absolute;left:37px;top:49px;font-size:8px;font-weight:500;color:#555}
.plink{position:absolute;top:52px;font-size:3.4px;font-weight:700;color:var(--lime-dark)}
.mainimg{position:absolute;left:37px;top:67px;width:230px;height:182px;border:1px solid var(--lime)}
.price{position:absolute;left:235px;top:73px;width:27px;height:17px;background:var(--lime);border:1.5px solid var(--white);outline:1px solid var(--lime);color:var(--white);font-size:8px;font-weight:500;display:flex;align-items:center;justify-content:center}
.thumbs{position:absolute;left:274px;top:67px;width:61px;height:181px}
.thumbs .cap{position:absolute;left:0;width:61px;height:8px;background:var(--lime);color:var(--white);font-size:5px;line-height:8px;text-align:center}
.thumb{position:absolute;left:24px;width:14px;height:20px;background:linear-gradient(#3a3a3a,#151515)}
.swatch{position:absolute;top:258px;width:15px;height:15px;border-radius:50%}
.label-g{position:absolute;font-size:6.5px;font-weight:500;color:var(--lime-dark)}
.spec{position:absolute;left:44px;font-size:3.8px;line-height:2.6;color:#888}
.feat{position:absolute;left:44px;font-size:3.8px;color:#888;display:flex;align-items:center;gap:4px}
.feat i{width:4.5px;height:4.5px;border:1px solid var(--lime-dark);border-radius:50%}

.aside{position:absolute;left:344px;width:96px;background:var(--panel)}
.aside h4{position:absolute;left:0;width:96px;text-align:center;font-size:4.6px;font-weight:500}
.scard{position:absolute;left:7px;width:82px;height:70px;background:var(--white)}
.scard .ph{position:absolute;left:24px;top:8px;width:32px;height:40px}
.scard .tab{position:absolute;right:-6px;top:10px;width:10px;height:16px;background:var(--lime);border-radius:2px}
.scard p{position:absolute;left:0;top:54px;width:82px;text-align:center;font-size:3.2px;color:#999;line-height:1.5}
.deal{position:absolute;left:7px;width:82px;height:80px;background:var(--white)}
.deal .off{position:absolute;right:6px;top:6px;width:22px;height:22px;border-radius:50%;background:#e5252c;border:1.5px solid var(--white);outline:1px solid #e5252c;color:var(--white);font-size:5px;font-weight:700;line-height:1;display:flex;align-items:center;justify-content:center;text-align:center}

/* article page */
.atitle{position:absolute;left:37px;top:48px;font-size:8.5px;font-weight:400;color:#666}
.txt{position:absolute;font-size:4px;line-height:1.85;color:#8a8a8a}
.head{position:absolute;font-size:4.2px;font-weight:500;color:#555}
.greenbar{position:absolute;left:37px;width:5px;background:var(--lime)}
.num{position:absolute;width:38px;height:38px;border-radius:50%;background:var(--lime);color:var(--white);font-size:12px;font-weight:500;display:flex;align-items:center;justify-content:center}
.rcard{position:absolute;top:650px;width:128px;height:65px;background:var(--white);border:1px solid var(--line)}
.rcard .tab{position:absolute;left:0;top:2px;width:16px;height:20px;background:var(--lime);border-radius:0 3px 3px 0}
.rcard .ph{position:absolute;left:86px;top:3px;width:40px;height:30px}
.rcard h5{position:absolute;left:8px;top:30px;font-size:4px;font-weight:500;color:#666}
.rcard p{position:absolute;left:8px;top:37px;width:112px;font-size:3px;line-height:1.5;color:#aaa}
.rcard em{position:absolute;left:8px;top:54px;font-style:normal;font-size:3px;color:var(--purple)}
</style>
</head>
<body>
<div class="stage">

<!-- ================= HOMEPAGE ================= -->
<section class="page home">
  <header class="topbar">
    <div class="brand" style="left:37px;top:4px"><i></i><span>Velmor<br>Goods</span></div>
    <span class="toplink" style="left:145px">✆ +353 1 555 0140</span>
    <span class="toplink" style="left:215px">✆ +353 1 555 0177</span>
    <span class="toplink" style="left:290px">✉ sales@velmorgoods.ie</span>
    <div class="searchbox" style="left:137px;width:93px">Search Product</div>
    <div class="hbtn" style="left:237px;width:34px">CATEGORIES</div>
    <div class="hcircle" style="left:278px"></div>
    <div class="hbtn" style="left:296px;width:42px;background:var(--purple-dark);color:#fff;border:1px solid #fff">SEARCH</div>
    <div class="a" style="left:376px;top:3px;width:56px;height:27px;background:#fff;text-align:center">
      <div style="font-size:7px;font-weight:700;color:#333;letter-spacing:.6px;margin-top:4px">BRENFIELD</div>
      <div class="tiny" style="font-size:3px;line-height:1.3">manufacturer of the<br>Velmor Goods range</div>
    </div>
  </header>

  <div class="nav" style="left:37px;width:40px">HOME</div>
  <div class="nav" style="left:89px;width:39px">ABOUT US</div>
  <div class="nav" style="left:140px;width:40px">BLOGS</div>
  <div class="nav" style="left:190px;width:41px">PRODUCTS</div>
  <div class="nav on" style="left:242px;width:41px">CONTACT US</div>
  <div class="a" style="left:373px;top:50px;font-size:3.8px;font-weight:700;color:var(--lime-dark)">DOWNLOAD BROCHURE ⬚</div>

  <nav class="sidemenu">
    <div style="top:6px"><i></i>Health Care<b>›</b></div>
    <div style="top:20px"><i></i>Pedal Bins<b>›</b></div>
    <div style="top:34px"><i></i>Street Furniture<b>›</b></div>
    <div style="top:48px"><i></i>Recycling<b>›</b></div>
    <div style="top:62px"><i></i>Washroom<b>›</b></div>
    <div style="top:76px"><i></i>Hotel &amp; Catering<b>›</b></div>
    <div style="top:90px"><i></i>Office<b>›</b></div>
    <div style="top:104px;border:0"><i></i>Others<b>›</b></div>
  </nav>

  <div class="slider">
    <div class="slide-card" style="left:20px">
      <div class="ph" role="img" aria-label="Free standing recycling bins in red, blue and grey" style="background:linear-gradient(90deg,#c43 0 25%,#2a6fc1 25% 50%,#2a6fc1 50% 75%,#333 75%)"></div>
      <p>Free Standing &amp; Wall/Pole<br>Mounted Litter Bins</p><em>Learn More</em>
    </div>
    <div class="slide-card" style="left:110px">
      <div class="ph" role="img" aria-label="White custom recycling bin units" style="background:linear-gradient(#eee,#cfcfcf)"></div>
      <p>Custom Made<br>Recycle Bin</p><em>Learn More</em>
    </div>
    <div class="slide-card" style="left:200px">
      <div class="ph" role="img" aria-label="Healthcare bins in green, yellow and white" style="background:linear-gradient(90deg,#e6e6e6 0 35%,#7dc142 35% 70%,#f2d21b 70%)"></div>
      <p>Healthcare Bin<br>Ranges</p><em>Learn More</em>
    </div>
    <span class="dot" style="left:137px;top:116px"></span><span class="dot" style="left:144px;top:116px"></span><span class="dot" style="left:151px;top:116px"></span>
  </div>

  <h2 class="sect" style="left:37px;top:224px">ABOUT US</h2>
  <div class="a small" style="left:37px;top:245px;width:265px;font-size:4.6px;line-height:1.55">
    <p>Velmor Goods is a range of products manufactured by Brenfield Engineering Holdings. Established in 1986, we have a reputation for producing the highest quality products in our industry, using environmentally friendly production methods.</p>
    <p style="margin-top:6px">We are the supplier of choice for the healthcare industry with products such as bins, trolleys, first aid products and soap dispensers.</p>
    <p style="margin-top:6px">Our range of street furniture can be seen across public spaces in Ireland. Products include litter bins, bicycle stands, ashbins, bollards and smoking shelters.</p>
    <p style="margin-top:6px">We supply recycling stations and recycling bins with a bespoke customization and design service.</p>
    <p style="margin-top:6px">Contact Ireland's leading suppliers of healthcare products, street furniture, and recycling stations today for an obligation free quotation.</p>
  </div>
  <div class="social">
    <div class="tile" style="left:20px;top:14px"><i></i><span>Velmor Goods</span></div>
    <div class="tile" style="left:70px;top:14px"><i></i><span>Brenfield Eng.</span></div>
    <div class="tile" style="left:20px;top:46px"><i></i><span>Velmor Goods</span></div>
    <div class="tile" style="left:70px;top:46px"><i></i><span>Brenfield Eng.</span></div>
    <div class="tile on" style="left:20px;top:78px"><i></i><span>Velmor Goods</span></div>
  </div>
  <div class="btn outline" style="left:37px;top:369px;width:53px">NEWS AND BLOGS</div>
  <div class="btn fill" style="left:100px;top:369px;width:53px">BUY A PRODUCT</div>

  <div class="feature" style="left:37px"><span class="corner"></span><div class="icon"></div>
    <h3>PRODUCT CATALOGUE</h3>
    <div class="ph" role="img" aria-label="Product catalogue cover" style="background:linear-gradient(#6b5a8a,#c6b07a)"></div>
    <p>Velmor Goods is a brand developed by Brenfield Engineering to showcase the most popular range of products we manufacture.</p><b>DOWNLOAD PRODUCT CATALOGUE</b></div>
  <div class="feature" style="left:172px"><span class="corner"></span><div class="icon"></div>
    <h3>BRENFIELD MANUFACTURING</h3>
    <div class="ph" role="img" aria-label="Manufacturing brochure cover" style="background:linear-gradient(#2a4d8f,#c0392b)"></div>
    <p>Brenfield Engineering were established in 1986 as a specialist, precision manufacturer working closely with customers to develop products to meet specific needs.</p><b>LEARN MORE</b></div>
  <div class="feature" style="left:308px"><span class="corner"></span><div class="icon"></div>
    <h3>THE HUB</h3>
    <div class="ph" role="img" aria-label="The Hub information centre cover" style="background:linear-gradient(#ffffff,#3b6fc4)"></div>
    <p>The Hub is the information center for the information required for the products of Velmor Goods, providing information relating to the quality standard as well.</p><b>ENTER THE HUB</b></div>

  <div class="companies"><span class="tri"></span></div>
  <h2 class="sect center" style="top:585px;font-size:7.5px">COMPANIES USING OUR PRODUCTS</h2>
  <div class="a" style="left:43px;top:614px;font-size:12px;color:var(--purple)">‹</div>
  <div class="a" style="left:423px;top:614px;font-size:12px;color:var(--purple)">›</div>
  <div class="company" style="left:69px">Corvane</div>
  <div class="company" style="left:138px">Halbrook</div>
  <div class="company" style="left:207px">Tessaro</div>
  <div class="company" style="left:277px">Lundmark</div>
  <div class="company" style="left:347px">Orvella</div>
  <div class="a" style="left:57px;top:654px;width:360px;height:1px;background:#d7b6dd"></div>
  <div class="a" style="left:235px;top:652px;width:5px;height:5px;border-radius:50%;background:var(--purple)"></div>

  <div class="blogband"></div>
  <h2 class="sect center" style="top:724px">OUR BLOG</h2>
  <article class="blogcard" style="left:37px">
    <div class="ph" role="img" aria-label="Black outdoor litter bin in a park" style="background:linear-gradient(#9fb97a,#4f7a2e)"></div>
    <h4>3 reasons to invest in outdoor litter bins</h4>
    <p class="tiny">Outdoor litter bins help keep the local environment clean, tidy and rubbish free. Many councils are installing numerous bins across their jurisdictions, realising the...</p>
    <em>read more</em></article>
  <article class="blogcard" style="left:172px">
    <div class="ph" role="img" aria-label="Office recycling bin units" style="background:linear-gradient(#d9c9a8,#8a7a5c)"></div>
    <h4>Waste prevention in the office</h4>
    <p class="tiny">Recycling has a number of environmental benefits, including reducing the amount of waste going into landfill, reducing pollution and conserving natural resources. It can also help...</p>
    <em>read more</em></article>
  <article class="blogcard" style="left:308px">
    <div class="ph" role="img" aria-label="Litter bins for parks" style="background:linear-gradient(#cfd6dc,#3a3a3a)"></div>
    <h4>Bins for parks</h4>
    <p class="tiny">Litter bins for parks, public spaces and other outdoor areas in Ireland come in a wide range of shapes and sizes. Bin sizes can range from 50 litres right up to 120 litres and various...</p>
    <em>read more</em></article>
  <div class="btn outline" style="left:211px;top:905px;width:51px;height:12px;font-weight:400;font-size:4px">EXPLORE ALL</div>

  <h2 class="sect center" style="top:967px">PRODUCTS</h2>
  <!-- row 1 -->
  <div class="pcard" style="left:37px;top:993px"><div class="ph" role="img" aria-label="Black three way recycling station" style="background:radial-gradient(circle at 50% 50%,#333 0 22%,#f6f6f6 23%)"></div><div class="strip"><i></i><i></i><i></i><i></i><i></i></div><span class="stars">★★★★★</span><span class="rev">11 REVIEWS</span><h5>3 WAY PLASTIC RECYCLING STATION</h5><p>Ideal for a wide range of internal waste recycling situations. Posters are easy to change behind the clear... more</p></div>
  <div class="pcard" style="left:139px;top:993px"><div class="ph" role="img" aria-label="Steel canteen tray trolley" style="background:linear-gradient(90deg,#f6f6f6 40%,#aaa 40% 60%,#f6f6f6 60%)"></div><div class="strip"><i></i><i></i><i></i><i></i><i></i></div><span class="stars">★★★★</span><span class="rev">9 REVIEWS</span><h5>CANTEEN TRAY TROLLEY</h5><p>All colours available. See sample colour chart. Stainless steel available as standard. Labelling can be... more</p></div>
  <div class="pcard" style="left:240px;top:993px"><div class="ph" role="img" aria-label="Large healthcare bin in white and red" style="background:linear-gradient(90deg,#f6f6f6 30%,#3a8fd8 30% 50%,#e04040 50% 70%,#f6f6f6 70%)"></div><div class="strip"><i></i><i></i><i></i><i></i><i></i></div><span class="stars">★★★★★</span><span class="rev">12 REVIEWS</span><h5>LARGE HEALTHCARE BIN 70L</h5><p>Large healthcare bin 70L in fire retardant cert. BS 476. Front access door will enable grain easy... more</p></div>
  <div class="pcard" style="left:341px;top:993px"><div class="ph" role="img" aria-label="Large grey pedal bin" style="background:linear-gradient(90deg,#f6f6f6 38%,#b7bfc6 38% 62%,#f6f6f6 62%)"></div><div class="strip"><i></i><i></i><i></i><i></i><i></i></div><span class="stars">★★★★★</span><span class="rev">13 REVIEWS</span><h5>LARGE PEDAL BIN</h5><p>Large pedal bins are manufactured from zintec pre-coated steel. They are polyester powder coated to... more</p></div>
  <!-- row 2 -->
  <div class="pcard" style="left:37px;top:1125px"><div class="ph" role="img" aria-label="Medical dispensing trolley" style="background:linear-gradient(#f6f6f6 25%,#999 25% 32%,#f6f6f6 32% 70%,#999 70% 76%,#f6f6f6 76%)"></div><div class="strip"><i></i><i></i><i></i><i></i><i></i></div><span class="stars">★★★★</span><span class="rev">12 REVIEWS</span><h5>MEDICAL DISPENSING TROLLEY</h5><p>All colours available. See sample colour chart. Stainless steel also available as standard. Labelling can... more</p></div>
  <div class="pcard" style="left:139px;top:1125px"><div class="ph" role="img" aria-label="Yellow sharps bin trolley" style="background:linear-gradient(90deg,#f6f6f6 38%,#f2d21b 38% 62%,#f6f6f6 62%)"></div><div class="strip"><i></i><i></i><i></i><i></i><i></i></div><span class="stars">★★★★</span><span class="rev">16 REVIEWS</span><h5>SHARPS 60/22L BIN TROLLEY</h5><p>Manufactured in zintec pre-coated steel. Polyester powder coated in signal yellow. All colours &amp; finishes... more</p></div>
  <div class="pcard" style="left:240px;top:1125px"><div class="ph" role="img" aria-label="L type nitrogen trolley" style="background:linear-gradient(135deg,#f6f6f6 40%,#b0b0b0 40% 46%,#f6f6f6 46%)"></div><div class="strip"><i></i><i></i><i></i><i></i><i></i></div><span class="stars">★★★★★</span><span class="rev">17 REVIEWS</span><h5>L TYPE NITROGEN TROLLEY</h5><p>All colours available. See sample colour chart. RAL... more</p></div>
  <div class="pcard" style="left:341px;top:1125px"><div class="ph" role="img" aria-label="Blue single linen trolley" style="background:linear-gradient(90deg,#f6f6f6 38%,#2a3fb8 38% 62%,#f6f6f6 62%)"></div><div class="strip"><i></i><i></i><i></i><i></i><i></i></div><span class="stars">★★★★★</span><span class="rev">13 REVIEWS</span><h5>SINGLE LINEN TROLLEY</h5><p>Lids can be colour coded to suit all requirements. All colours are... more</p></div>

  <div class="badge" style="left:91px;width:47px"></div>
  <div class="badge" style="left:157px;width:40px"></div>
  <div class="badge" style="left:216px;width:40px;border-radius:4px"></div>
  <div class="badge" style="left:281px;width:40px;border-radius:50%"></div>
  <div class="badge" style="left:343px;width:40px;border-radius:50%"></div>

  <footer class="footer" style="top:1371px;height:129px">
    <div class="brand" style="top:17px;height:20px"><i style="width:9px;height:9px"></i><span style="font-size:5.5px">Velmor<br>Goods</span></div>
    <div class="addr" style="top:45px;width:80px">Brenfield Engineering Holdings Ltd<br>Unit 9 Harcourt Business Park<br>Drumcarrig<br>Co. Dublin</div>
    <div class="a" style="left:38px;top:86px;color:#fff;font-size:7px">✆</div>
    <div class="addr" style="top:104px">+353 (0)1 555 0140</div>
    <h6 style="left:144px;top:16px">PRODUCTS</h6>
    <div class="links" style="left:144px;top:28px">HEALTHCARE<br>PEDAL BINS<br>STREET FURNITURE<br>RECYCLING<br>WASHROOM<br>HOTEL AND CATERING<br>OFFICE</div>
    <h6 style="left:216px;top:16px">BLOGS</h6>
    <div class="links" style="left:216px;top:28px">INVEST IN OUTDOOR LITTER BINS<br>WASTE PREVENTION<br>PLASTIC HEALTHCARE BINS<br>INFECTION CONTROL</div>
    <h6 style="left:308px;top:16px">CONTACT</h6>
    <div class="field" style="left:308px;top:29px;width:62px">First Name</div>
    <div class="field" style="left:378px;top:29px;width:60px">Last Name</div>
    <div class="field" style="left:308px;top:46px;width:62px">Email</div>
    <div class="field" style="left:378px;top:46px;width:60px">Phone Number</div>
    <div class="field" style="left:308px;top:62px;width:130px;height:34px">Your Message</div>
    <div class="send" style="left:308px;top:103px">CONTACT US</div>
    <div class="copy" style="top:121px">ALL COPYRIGHTS RESERVED © 2019</div>
  </footer>
</section>

<!-- ================= PRODUCT PAGE ================= -->
<section class="page product">
  <header class="topbar">
    <div class="brand" style="left:44px;top:4px"><i></i><span>Velmor<br>Goods</span></div>
    <span class="toplink" style="left:345px;top:14px">👤 PROFILE</span>
    <span class="toplink" style="left:374px;top:14px">🛒 VIEW CART</span>
    <span class="toplink" style="left:408px;top:14px">➦ CHECKOUT</span>
  </header>

  <h1 class="ptitle">3 WAY PLASTIC RECYCLING STATION</h1>
  <span class="plink" style="left:242px">ADD TO FAVOURITE</span>
  <span class="plink" style="left:305px">ADD TO CART</span>

  <div class="mainimg">
    <span class="a" style="left:6px;top:4px;font-size:4.5px;color:var(--lime-dark);letter-spacing:.5px">★★★★★</span>
    <div class="a" role="img" aria-label="Black three way plastic recycling station with green centre lid" style="left:60px;top:18px;width:106px;height:140px;border-radius:22px 22px 8px 8px;background:linear-gradient(90deg,#1a1a1a 0 33%,#2c2c2c 33% 34%,#1f1f1f 34% 100%)"></div>
    <div class="a" style="left:96px;top:22px;width:34px;height:18px;border-radius:6px;background:#6cc330"></div>
  </div>
  <div class="price">$99</div>

  <div class="thumbs">
    <div class="cap" style="top:0">⌃</div>
    <div class="thumb" style="top:18px" role="img" aria-label="Recycling station thumbnail"></div>
    <div class="thumb" style="top:51px" role="img" aria-label="Recycling station thumbnail"></div>
    <div class="thumb" style="top:83px" role="img" aria-label="Recycling station thumbnail"></div>
    <div class="thumb" style="top:116px" role="img" aria-label="Recycling station thumbnail"></div>
    <div class="thumb" style="top:146px;width:20px;left:21px;height:14px" role="img" aria-label="Recycling station thumbnail"></div>
    <div class="a" style="left:5px;top:84px;font-size:7px;color:var(--lime-dark)">«</div>
    <div class="cap" style="top:173px">⌄</div>
  </div>

  <span class="swatch" style="left:45px;background:#9bc02a"></span>
  <span class="swatch" style="left:72px;background:#1ea6ef"></span>
  <span class="swatch" style="left:99px;background:#ffd21a"></span>
  <span class="swatch" style="left:126px;background:#ee1f4d"></span>
  <span class="swatch" style="left:153px;background:#111;color:#fff;font-size:8px;display:flex;align-items:center;justify-content:center">✓</span>

  <span class="label-g" style="left:44px;top:292px">DETAILS</span>
  <span class="plink" style="left:282px;top:293px">🛒 ADD TO CART</span>
  <p class="txt" style="left:44px;top:306px;width:222px;font-size:3.8px">Manufactured from high impact plastic. 3 bag holders. Ideal for a wide range of internal waste recycling situations. Posters are easy to change behind the clear acrylic window. Sack retaining feature for discreet fitting of refuse bag. Colour coded apertures and graphics as standard. Area available for personalised graphic or company logo. Slim body profile makes it ideal for placement along corridors and narrow walkways. Easy to fit externally mounted. A3 signage kit are available, click here for more information. Interchangeable lids allow bespoke waste streams to suit your needs.</p>

  <span class="label-g" style="left:44px;top:387px">DIMENSIONS</span>
  <div class="spec" style="top:399px">HEIGHT : 950 mm<br>WIDTH : 580 mm<br>DEPTH : 400 mm</div>

  <span class="label-g" style="left:44px;top:442px">FEATURES</span>
  <div class="feat" style="top:460px"><i></i>Feature number 1</div>
  <div class="feat" style="top:470px"><i></i>Feature number 2</div>
  <div class="feat" style="top:480px"><i></i>Feature number 3</div>
  <div class="feat" style="top:490px"><i></i>Feature number 4</div>
  <div class="btn fill" style="left:44px;top:507px;width:30px;height:10px;background:var(--lime);font-size:3.4px">BUY NOW</div>

  <aside class="aside" style="top:67px;height:343px">
    <h4 style="top:10px;color:var(--lime-dark)">SIMILAR PRODUCTS</h4>
    <div class="scard" style="top:24px"><div class="ph" role="img" aria-label="Yellow sharps bin trolley" style="background:linear-gradient(90deg,#fff 30%,#f2d21b 30% 70%,#fff 70%)"></div><span class="tab"></span><p>SHARPS 60/22L BIN<br>TROLLEY</p></div>
    <div class="scard" style="top:104px"><div class="ph" role="img" aria-label="Medical dispensing trolley" style="background:linear-gradient(135deg,#dfeaf4,#9fb6cc)"></div><span class="tab"></span><p>MEDICAL DISPENSING<br>TROLLEY</p></div>
    <div class="scard" style="top:182px"><div class="ph" role="img" aria-label="Yellow pedal bin" style="background:linear-gradient(90deg,#fff 20%,#f2df2a 20% 80%,#fff 80%)"></div><span class="tab"></span><p>PEDAL BINS</p></div>
    <div class="scard" style="top:260px"><div class="ph" role="img" aria-label="Large healthcare bins" style="background:linear-gradient(#f0f0f0,#b9c2c9)"></div><span class="tab"></span><p>LARGE HEALTHCARE<br>BINS 70L</p></div>
  </aside>
  <aside class="aside" style="top:416px;height:109px">
    <h4 style="top:7px;color:var(--purple)">DEAL OF THE DAY</h4>
    <div class="deal" style="top:25px">
      <div class="a" role="img" aria-label="Canteen trolley" style="left:28px;top:14px;width:24px;height:46px;background:linear-gradient(#f6f6f6 15%,#555 15% 55%,#aaa 55%)"></div>
      <span class="off">30%<br>OFF</span>
      <p class="a tiny" style="left:0;top:66px;width:82px;text-align:center;font-size:3.2px">CANTEEN TROLLEY</p>
    </div>
  </aside>

  <footer class="footer" style="top:550px;height:130px">
    <div class="brand" style="top:17px;height:20px"><i style="width:9px;height:9px"></i><span style="font-size:5.5px">Velmor<br>Goods</span></div>
    <div class="addr" style="top:45px;width:80px">Brenfield Engineering Holdings Ltd<br>Unit 9 Harcourt Business Park<br>Drumcarrig<br>Co. Dublin</div>
    <div class="a" style="left:38px;top:88px;color:#fff;font-size:7px">✆</div>
    <div class="addr" style="top:105px">+353 (0)1 555 0140</div>
    <h6 style="left:144px;top:16px">PRODUCTS</h6>
    <div class="links" style="left:144px;top:28px">HEALTHCARE<br>PEDAL BINS<br>STREET FURNITURE<br>RECYCLING<br>WASHROOM<br>HOTEL AND CATERING<br>OFFICE</div>
    <h6 style="left:216px;top:16px">BLOGS</h6>
    <div class="links" style="left:216px;top:28px">INVEST IN OUTDOOR LITTER BINS<br>WASTE PREVENTION<br>PLASTIC HEALTHCARE BINS<br>INFECTION CONTROL</div>
    <h6 style="left:308px;top:16px">CONTACT</h6>
    <div class="field" style="left:308px;top:29px;width:62px">First Name</div>
    <div class="field" style="left:378px;top:29px;width:60px">Last Name</div>
    <div class="field" style="left:308px;top:46px;width:62px">Email</div>
    <div class="field" style="left:378px;top:46px;width:60px">Phone Number</div>
    <div class="field" style="left:308px;top:62px;width:130px;height:34px">Your Message</div>
    <div class="send" style="left:308px;top:104px">CONTACT US</div>
    <div class="copy" style="top:122px">ALL COPYRIGHTS RESERVED © 2019</div>
  </footer>
</section>

<!-- ================= ARTICLE PAGE ================= -->
<section class="page article">
  <header class="topbar">
    <div class="brand" style="left:44px;top:4px"><i></i><span>Velmor<br>Goods</span></div>
    <span class="toplink" style="left:235px">✆ +353 1 555 0140</span>
    <span class="toplink" style="left:305px">✆ +353 1 555 0177</span>
    <span class="toplink" style="left:375px">✉ sales@velmorgoods.ie</span>
    <div class="searchbox" style="left:237px;width:90px">Search Product</div>
    <div class="hbtn" style="left:333px;width:34px">CATEGORIES</div>
    <div class="hcircle" style="left:374px"></div>
    <div class="hbtn" style="left:394px;width:42px;background:var(--purple-dark);color:#fff;border:1px solid #fff">SEARCH</div>
  </header>

  <h1 class="atitle">3 reasons to invest in outdoor litter bins</h1>
  <p class="txt" style="left:37px;top:66px;width:150px">Outdoor litter bins help keep the local environment clean, tidy and rubbish free. Many councils are installing numerous bins across their jurisdictions, realising the strong link between the number of bins and the reduction in the amount of litter left on the ground.</p>
  <p class="txt" style="left:37px;top:122px;width:150px">Ashgrove and Kilbarra County Council are just two councils that have installed our bins and in doing so are helping to reduce the amount of waste strewn on the ground in their public spaces.</p>
  <div class="a" role="img" aria-label="Black and gold outdoor litter bin on a park lawn" style="left:197px;top:69px;width:137px;height:96px;background:linear-gradient(#b8c99a 0%,#7e9a52 45%,#4d7326 100%)"></div>

  <div class="greenbar" style="top:177px;height:73px"></div>
  <div class="head" style="left:54px;top:176px">COMPLY WITH HEALTH AND SAFETY</div>
  <p class="txt" style="left:54px;top:185px;width:245px">Minimising the amount of rubbish left lying on the ground not only improves the appearance of public areas, it also reduces the risk to health and safety. By having a safe place for people to dispose of their rubbish, the risk of stepping on broken glass and other potentially harmful items reduces dramatically.</p>
  <p class="txt" style="left:54px;top:233px;width:245px">This is especially important if the public space is being frequented by families, such as a shelter playing in a playground.</p>
  <div class="num" style="left:296px;top:196px">1</div>

  <div class="greenbar" style="top:260px;height:120px"></div>
  <div class="head" style="left:54px;top:259px">BOOST CIVIC PRIDE</div>
  <p class="txt" style="left:54px;top:268px;width:245px">If you are a council that is serious about helping residents enjoy their neighbourhood, installing outdoor rubbish bins should be the first step to improving their local environment.</p>
  <p class="txt" style="left:54px;top:297px;width:245px">Research has shown the amount of littering directly related to the number of bins available to dispose of the rubbish. Therefore, through the installation of outdoor litter bins, the environment is more likely to be kept litter free.</p>
  <p class="txt" style="left:54px;top:335px;width:245px">If the community frequents an area that is already spoilt with a lot of rubbish littered on the ground, they will be more inclined to add to the rubbish problem. However, if the area is kept pristine thanks to the use of outdoor litter bins, local residents are much more likely to pop their rubbish into the bin and feel better about the area they and their family live in.</p>
  <div class="num" style="left:296px;top:303px">2</div>

  <div class="greenbar" style="top:382px;height:130px"></div>
  <div class="head" style="left:54px;top:381px">DO YOUR BIT FOR THE ENVIRONMENT</div>
  <p class="txt" style="left:54px;top:390px;width:245px">Recycling is important in order to reduce greenhouse gases and limit the amount of waste that ends up in the oceans and which can be harmful to wildlife. You can even be seen as a forward thinking council by investing in recycling bins for your public spaces which improves your reputation and carbon footprint.</p>
  <p class="txt" style="left:54px;top:437px;width:245px">Recycling has been proven to not only reduce landfill waste but lead to a reduction in water and air pollution, having a positive effect on the global climate.</p>
  <p class="txt" style="left:54px;top:465px;width:245px">All products that end up in landfill have a negative impact, with more trucks needed to transport the waste, and more energy needed to dispose of the rubbish.</p>
  <p class="txt" style="left:54px;top:494px;width:245px">By recycling and re-using our rubbish, we can reduce this impact on the environment. Recycling can even involve converting waste materials into fuel or other energy sources.</p>
  <div class="num" style="left:296px;top:433px">3</div>

  <div class="head" style="left:37px;top:526px">OUTDOOR LITTER BINS WE OFFER</div>
  <p class="txt" style="left:37px;top:535px;width:295px">We offer a large range of outdoor litter bins to suit all of your council's needs. We have plastic and metal bins, open-topped bins and pyramid top bins. For placing outside offices, shops, amenities and other public areas, rubbish bins with built-in ashtrays and two compartment bins which cater for all of your disposal needs.</p>
  <p class="txt" style="left:37px;top:574px;width:295px">Our bins feature special non-resistant primer and powder coating to keep them protected from all weather situations.</p>
  <p class="txt" style="left:37px;top:593px;width:295px">Thanks to the high-quality fabrication of our bins, we can ensure our bins are going to stand the test of time.</p>
  <p class="txt" style="left:37px;top:612px;width:310px">Interested in installing outdoor litter bins? Contact us (https://www.velmorgoods.ie/contact-us) for more information.</p>
  <div class="a" style="left:37px;top:635px;font-size:4.2px;color:var(--lime-dark)">Related articles</div>
  <div class="rcard" style="left:37px"><span class="tab"></span><div class="ph" role="img" aria-label="Office recycling bins" style="background:linear-gradient(90deg,#3a3a3a 0 30%,#d8c9a8 30% 70%,#3a6fc1 70%)"></div><h5>WASTE PREVENTION IN OFFICE</h5><p>Recycling has a number of environmental benefits, including reducing the amount of waste going into landfill.</p><em>full article</em></div>
  <div class="rcard" style="left:172px"><span class="tab"></span><div class="ph" role="img" aria-label="Coloured recycling bins" style="background:linear-gradient(90deg,#e04040 0 30%,#f2d21b 30% 65%,#6cc330 65%)"></div><h5>ARTICLE NUMBER 2</h5><p>Short article summary about healthcare bins and related products, with links to the range in full.</p><em>full article</em></div>

  <aside class="aside" style="left:347px;top:69px;height:341px;width:93px">
    <h4 style="top:10px;width:93px;color:var(--lime-dark)">BROWSE OUR PRODUCTS</h4>
    <div class="scard" style="top:26px;width:80px"><div class="ph" role="img" aria-label="Yellow sharps bin trolley" style="background:linear-gradient(90deg,#fff 30%,#f2d21b 30% 70%,#fff 70%)"></div><span class="tab"></span><p style="width:80px">SHARPS 60/22L BIN<br>TROLLEY</p></div>
    <div class="scard" style="top:107px;width:80px"><div class="ph" role="img" aria-label="Medical dispensing trolley" style="background:linear-gradient(135deg,#dfeaf4,#9fb6cc)"></div><span class="tab"></span><p style="width:80px">MEDICAL DISPENSING<br>TROLLEY</p></div>
    <div class="scard" style="top:185px;width:80px"><div class="ph" role="img" aria-label="Yellow pedal bin" style="background:linear-gradient(90deg,#fff 20%,#f2df2a 20% 80%,#fff 80%)"></div><span class="tab"></span><p style="width:80px">PEDAL BINS</p></div>
    <div class="scard" style="top:262px;width:80px"><div class="ph" role="img" aria-label="Large healthcare bins" style="background:linear-gradient(#f0f0f0,#b9c2c9)"></div><span class="tab"></span><p style="width:80px">LARGE HEALTHCARE<br>BINS 70L</p></div>
  </aside>
  <aside class="aside" style="left:347px;top:418px;height:109px;width:93px">
    <h4 style="top:7px;width:93px;color:var(--purple)">DEAL OF THE DAY</h4>
    <div class="deal" style="top:25px;width:80px">
      <div class="a" role="img" aria-label="Canteen trolley" style="left:28px;top:14px;width:24px;height:46px;background:linear-gradient(#f6f6f6 15%,#555 15% 55%,#aaa 55%)"></div>
      <span class="off">30%<br>OFF</span>
      <p class="a tiny" style="left:0;top:66px;width:80px;text-align:center;font-size:3.2px">CANTEEN TROLLEY</p>
    </div>
  </aside>

  <footer class="footer" style="top:733px;height:129px">
    <div class="brand" style="top:17px;height:20px"><i style="width:9px;height:9px"></i><span style="font-size:5.5px">Velmor<br>Goods</span></div>
    <div class="addr" style="top:45px;width:80px">Brenfield Engineering Holdings Ltd<br>Unit 9 Harcourt Business Park<br>Drumcarrig<br>Co. Dublin</div>
    <div class="a" style="left:38px;top:88px;color:#fff;font-size:7px">✆</div>
    <div class="addr" style="top:104px">+353 (0)1 555 0140</div>
    <h6 style="left:144px;top:16px">PRODUCTS</h6>
    <div class="links" style="left:144px;top:28px">HEALTHCARE<br>PEDAL BINS<br>STREET FURNITURE<br>RECYCLING<br>WASHROOM<br>HOTEL AND CATERING<br>OFFICE</div>
    <h6 style="left:216px;top:16px">BLOGS</h6>
    <div class="links" style="left:216px;top:28px">INVEST IN OUTDOOR LITTER BINS<br>WASTE PREVENTION<br>PLASTIC HEALTHCARE BINS<br>INFECTION CONTROL</div>
    <h6 style="left:308px;top:16px">CONTACT</h6>
    <div class="field" style="left:308px;top:29px;width:62px">First Name</div>
    <div class="field" style="left:378px;top:29px;width:60px">Last Name</div>
    <div class="field" style="left:308px;top:46px;width:62px">Email</div>
    <div class="field" style="left:378px;top:46px;width:60px">Phone Number</div>
    <div class="field" style="left:308px;top:62px;width:130px;height:34px">Your Message</div>
    <div class="send" style="left:308px;top:103px">CONTACT US</div>
    <div class="copy" style="top:121px">ALL COPYRIGHTS RESERVED © 2019</div>
  </footer>
</section>

</div>
</body>
</html>
```